Harbor Lantern Business Card

I need a business card for my firearm business. On one side I want the Harbor Lantern skull logo with the writing (tag on LLC at the end of Harbor Lantern). I want it to be dark, sharp, and look professional. I would like a small American flag in the corner of the card also. The other side of the card is where I want all the info. The info I want on the card will be my contact info as well as what kind of business it is. The contact info is:
Noel Varga
Founder and Owner
n.varga@harborlantern.example
555-204-7318
I want the Harbor Lantern logo with just the skull on this side also.The info I want about the business is:
- Class Three Dealer
- Certified Gunsmith/Armorer
- Certified Firearm Instructor
If you can give the background a gothic but professional feel that would be great! Hope we can work together on this and I look forward to hearing from you soon. Thank you!
Target Market(s)
Firearms, guns, training, gunsmithing
Industry/Entity Type
Gun
Contact Information for Business Card
Noel Varga
Founder and Owner
555-204-7318
- Class Three Dealer

```html
<!DOCTYPE html>
<html lang="en">
<head>
<meta charset="utf-8">
<title>Harbor Lantern Business Card</title>
<link href="https://fonts.googleapis.com/css2?family=PT+Sans:wght@400;700&family=PT+Sans+Narrow:wght@400;700&display=swap" rel="stylesheet">
<style>
  :root {
    --page: #f1f1f1;
    --ink: #0b0b0b;
    --panel: #9b9b9b;
    --stripe: #a9a9a9;
    --star: #f4f4f4;
    --text-light: #e9e9e9;
    --text-dark: #111111;
    --steel: #6c6c6c;
    --steel-dark: #4e4e4e;
  }
  html, body {
    margin: 0;
    width: 1200px;
    height: 892px;
    overflow: hidden;
    background: var(--page);
  }
  .canvas {
    position: relative;
    width: 1200px;
    height: 892px;
  }

  /* Contact side */
  .card-front {
    position: absolute;
    left: 70px;
    top: 240px;
    width: 560px;
    height: 320px;
    background: var(--ink);
    box-shadow: 0 10px 24px rgba(0,0,0,0.18);
    font-family: "PT Sans", sans-serif;
  }
  .front-panel {
    position: absolute;
    left: 22px;
    top: 44px;
    width: 516px;
    height: 252px;
    background: var(--panel);
  }
  .flag-corner {
    position: absolute;
    right: 0;
    top: 0;
    width: 300px;
    height: 110px;
  }
  .brand {
    position: absolute;
    left: 140px;
    top: 30px;
    display: flex;
    align-items: center;
    gap: 10px;
  }
  .brand-mark {
    width: 28px;
    height: 28px;
    border-radius: 50%;
    background: var(--ink);
  }
  .brand-name {
    font-weight: 700;
    font-size: 21px;
    letter-spacing: 2px;
    color: var(--text-dark);
    text-transform: uppercase;
  }
  .divider {
    position: absolute;
    left: 0;
    top: 78px;
    width: 310px;
    height: 2px;
    background: var(--ink);
  }
  .services {
    position: absolute;
    right: 14px;
    top: 70px;
    width: 178px;
    padding: 8px 10px;
    background: #1e1e1e;
    color: var(--text-light);
    font-size: 14px;
    line-height: 1.35;
    text-align: right;
  }
  .services p { margin: 0; }
  .person-name {
    position: absolute;
    left: 14px;
    top: 84px;
    margin: 0;
    font-family: "PT Sans Narrow", sans-serif;
    font-weight: 700;
    font-size: 30px;
    color: var(--text-dark);
  }
  .role {
    position: absolute;
    left: 8px;
    top: 128px;
    width: 170px;
    padding: 3px 8px;
    background: #2a2a2a;
    color: var(--text-light);
    font-size: 14px;
  }
  .phone {
    position: absolute;
    left: 8px;
    top: 160px;
    width: 190px;
    padding: 4px 8px;
    background: #1a1a1a;
    color: var(--text-light);
    font-size: 17px;
  }
  .email {
    position: absolute;
    left: 8px;
    bottom: 10px;
    width: 480px;
    padding: 4px 8px;
    background: #2a2a2a;
    color: var(--text-light);
    font-size: 17px;
    letter-spacing: 1.5px;
  }

  /* Brand side */
  .card-back {
    position: absolute;
    left: 760px;
    top: 180px;
    width: 340px;
    height: 540px;
    background: var(--ink);
    overflow: hidden;
    box-shadow: 0 10px 24px rgba(0,0,0,0.18);
  }
  .back-bands {
    position: absolute;
    inset: 0;
  }
  .back-brand {
    position: absolute;
    left: 0;
    right: 0;
    top: 200px;
    display: flex;
    flex-direction: column;
    align-items: center;
    gap: 16px;
  }
  .back-mark {
    width: 56px;
    height: 56px;
    border-radius: 50%;
    background: var(--steel);
  }
  .back-name {
    font-family: "PT Sans", sans-serif;
    font-weight: 700;
    font-size: 26px;
    letter-spacing: 3px;
    color: var(--steel);
    text-transform: uppercase;
  }
</style>
</head>
<body>
<div class="canvas">

  <section class="card-front">
    <div class="front-panel">
      <div class="brand">
        <span class="brand-mark"></span>
        <span class="brand-name">Harbor Lantern LLC</span>
      </div>
      <div class="divider"></div>
      <div class="services">
        <p>Class Three Dealer</p>
        <p>Gunsmith/Armorer</p>
        <p>Certified Firearm Instructor</p>
      </div>
      <h1 class="person-name">Noel Varga</h1>
      <div class="role">Founder and Owner</div>
      <div class="phone">P: 555-204-7318</div>
      <div class="email">E: n.varga@harborlantern.example</div>
    </div>

    <svg class="flag-corner" viewBox="0 0 300 110" role="img" aria-label="Small American flag in the card corner">
      <polygon points="60,0 300,0 300,20 90,44 20,44" fill="var(--ink)"/>
      <polygon points="120,0 160,0 40,44 10,44" fill="var(--stripe)"/>
      <polygon points="175,0 205,0 100,44 70,44" fill="var(--stripe)"/>
      <polygon points="220,0 245,0 150,44 125,44" fill="var(--stripe)"/>
      <polygon points="230,0 300,0 300,70" fill="var(--ink)"/>
      <g fill="var(--star)">
        <polygon points="250,14 252,19 257,19 253,22 255,27 250,24 245,27 247,22 243,19 248,19"/>
        <polygon points="272,14 274,19 279,19 275,22 277,27 272,24 267,27 269,22 265,19 270,19"/>
        <polygon points="261,26 263,31 268,31 264,34 266,39 261,36 256,39 258,34 254,31 259,31"/>
        <polygon points="283,26 285,31 290,31 286,34 288,39 283,36 278,39 280,34 276,31 281,31"/>
        <polygon points="272,38 274,43 279,43 275,46 277,51 272,48 267,51 269,46 265,43 270,43"/>
        <polygon points="290,4 291,8 295,8 292,10 293,14 290,12 287,14 288,10 285,8 289,8"/>
      </g>
    </svg>
  </section>

  <section class="card-back">
    <svg class="back-bands" width="340" height="540" viewBox="0 0 340 540" aria-hidden="true">
      <circle cx="170" cy="250" r="205" fill="none" stroke="var(--steel-dark)" stroke-width="34"/>
      <circle cx="170" cy="250" r="224" fill="none" stroke="var(--steel)" stroke-width="2" stroke-dasharray="2 8"/>
      <polygon points="0,400 170,490 340,400 340,428 170,518 0,428" fill="var(--steel)"/>
      <polygon points="0,445 170,535 340,445 340,468 170,558 0,468" fill="var(--steel)"/>
    </svg>
    <div class="back-brand">
      <span class="back-mark"></span>
      <span class="back-name">Harbor Lantern</span>
    </div>
  </section>

</div>
</body>
</html>
```